Energy drink company looking for a complete can design

Design an energy drink can label using an established trademarked logo along with mandatory nutrition and ingredients table.
We would like to see 3 versions or samples to judge:
1. can design over a black background - called dark color version
2. can design over a white background - called light color version
3. can design over a grey/silver background - called balanced color version

Target Market(s)

USA

Requirements
Must have
• the phrase "vex lumora energy drink" "vex lumora" and "ALL Natural Libido Enhancing energy drink" must be on the can somewhere

```html
<!DOCTYPE html>
<html lang="en">
<head>
<meta charset="utf-8">
<title>vex lumora energy drink — can label versions</title>
<link href="https://fonts.googleapis.com/css2?family=Josefin+Sans:wght@600;700&family=Oswald:wght@300;400&family=Roboto+Condensed:wght@400;700&display=swap" rel="stylesheet">
<style>
  :root {
    --backdrop: #66686b;
    --label-white: #ffffff;
    --label-dark: #1b1716;
    --silver-1: #9c9ea1;
    --silver-2: #eceded;
    --silver-3: #b3b5b8;
    --ink: #1d1d1f;
    --ink-on-dark: #f3f3f3;
    --gold: #b8902b;
    --juice: #f3e37c;
    --lip-red: #c9212b;
    --lip-red-deep: #9f1820;
  }
  * { box-sizing: border-box; margin: 0; padding: 0; }
  html, body { width: 1200px; height: 900px; overflow: hidden; }
  body { background: var(--backdrop); position: relative; font-family: "Roboto Condensed", sans-serif; }

  /* ---------- front panel (shared by all versions) ---------- */
  .front-panel {
    position: absolute; overflow: hidden; color: var(--ink);
    --y-claim: 12.2%; --y-main: 16.3%; --y-brand: 53%; --y-type: 78%; --y-vol: 88.8%;
    --lips-top: 26%; --lips-h: 19.5%; --lips-w: 68%;
  }
  .front-panel .text-line {
    position: absolute; left: 0; right: 0; text-align: center;
    line-height: 1; white-space: nowrap; transform: translateY(-50%);
  }
  .claim-top  { top: var(--y-claim); font-family: "Josefin Sans", sans-serif; font-weight: 600; font-size: var(--fs-claim); letter-spacing: 0.16em; }
  .claim-main { top: var(--y-main); font-family: "Josefin Sans", sans-serif; font-weight: 700; font-size: var(--fs-main); letter-spacing: 0.07em; }
  .brand-name { top: var(--y-brand); font-family: "Oswald", sans-serif; font-weight: 300; font-size: var(--fs-brand); color: var(--gold); letter-spacing: -0.01em; }
  .product-type { top: var(--y-type); font-family: "Oswald", sans-serif; font-weight: 400; font-style: italic; font-size: var(--fs-type); letter-spacing: 0.08em; }
  .volume { top: var(--y-vol); font-family: "Oswald", sans-serif; font-weight: 300; font-size: var(--fs-vol); }

  .juice-splash { position: absolute; inset: 0; width: 100%; height: 100%; }
  .lips-art {
    position: absolute; top: var(--lips-top); height: var(--lips-h); width: var(--lips-w);
    left: calc((100% - var(--lips-w)) / 2); border-radius: 8px;
    background: linear-gradient(180deg, var(--lip-red), var(--lip-red-deep));
  }

  .size-small { --fs-claim: 7.6px; --fs-main: 9.2px; --fs-brand: 36px; --fs-type: 13px; --fs-vol: 12px; }
  .size-large { --fs-claim: 18px; --fs-main: 22px; --fs-brand: 84px; --fs-type: 31px; --fs-vol: 29px; }
  .size-label {
    --fs-claim: 8.8px; --fs-main: 11.5px; --fs-brand: 52px; --fs-type: 15px; --fs-vol: 14px;
    --y-claim: 12.5%; --y-main: 16.5%; --y-brand: 55.5%; --y-type: 83%; --y-vol: 94%;
    --lips-top: 27%; --lips-h: 21%; --lips-w: 28%;
  }

  .version-dark { background: var(--label-dark); color: var(--ink-on-dark); }
  .version-balanced { background: linear-gradient(90deg, var(--silver-1) 0%, var(--silver-2) 30%, var(--silver-3) 60%, var(--silver-2) 82%, var(--silver-1) 100%); }
  .version-light { background: var(--label-white); }

  /* ---------- placement ---------- */
  .can-dark     { left: 133px; top: 96px; width: 135px; height: 340px; }
  .can-balanced { left: 287px; top: 96px; width: 135px; height: 340px; }
  .can-light    { left: 440px; top: 96px; width: 135px; height: 340px; }
  .can-back     { position: absolute; left: 593px; top: 96px; width: 135px; height: 340px; background: var(--label-white); overflow: hidden; }
  .can-hero     { left: 780px; top: 60px; width: 321px; height: 786px; }

  .label-sheet { position: absolute; left: 182px; top: 495px; width: 497px; height: 351px; background: var(--label-white); overflow: hidden; }
  .label-sheet .front-panel { left: 0; top: 0; width: 392px; height: 351px; background: transparent; }

  /* ---------- nutrition panel ---------- */
  .info-block { position: absolute; transform-origin: top left; width: 233px; }
  .label-sheet .nf-block { left: 387px; top: 32px; transform: scale(0.44); }
  .label-sheet .ing-block { left: 387px; top: 270px; transform: scale(0.44); }
  .can-back .nf-block { left: 25px; top: 31px; transform: scale(0.373); }
  .can-back .ing-block { left: 25px; top: 245px; transform: scale(0.373); }

  .nutrition-facts {
    width: 233px; border: 1.5px solid var(--ink); padding: 3px 5px 4px; color: var(--ink);
    font-family: "Roboto Condensed", sans-serif; font-size: 10.5px; line-height: 1;
  }
  .nf-title { font-size: 27px; font-weight: 700; line-height: 1; letter-spacing: -0.3px; }
  .nf-row { display: flex; justify-content: space-between; border-top: 1px solid var(--ink); padding: 3.5px 0 3px; }
  .nf-row.indent { padding-left: 12px; }
  .nf-row.indent2 { padding-left: 24px; }
  .nf-row b { font-weight: 700; }
  .nf-thick { border-top: 9px solid var(--ink); }
  .nf-serving { font-weight: 700; font-size: 12px; border-top: none; }
  .nf-calories { display: flex; justify-content: space-between; align-items: flex-end; font-weight: 700; padding: 2px 0 3px; }
  .nf-calories .label { font-size: 9px; line-height: 1.2; }
  .nf-calories .label span { display: block; font-size: 19px; }
  .nf-calories .value { font-size: 30px; }
  .nf-dv { text-align: right; font-weight: 700; font-size: 9px; border-top: 4px solid var(--ink); padding: 3px 0; }
  .nf-footnote { font-size: 6.5px; line-height: 1.25; border-top: 4px solid var(--ink); padding-top: 3px; }

  .ingredients {
    font-family: "Roboto Condensed", sans-serif; font-size: 12px; line-height: 1.45;
    letter-spacing: 0.4px; text-align: justify; color: var(--ink);
  }
</style>
</head>
<body>

  <!-- dark colour version -->
  <section class="front-panel size-small version-dark can-dark">
    <svg class="juice-splash" viewBox="0 0 100 100" preserveAspectRatio="none" role="img" aria-label="Flowing pineapple juice splash">
      <path d="M0 8 C20 15 30 30 22 45 C16 58 30 64 45 68 C60 72 78 70 100 78 L100 86 C78 80 58 82 42 78 C24 74 8 64 12 48 C16 34 10 22 0 18 Z" fill="var(--juice)" opacity="0.7"/>
    </svg>
    <div class="lips-art" role="img" aria-label="Illustration of red lips biting a pineapple slice"></div>
    <p class="text-line claim-top">ALL NATURAL</p>
    <p class="text-line claim-main">LIBIDO ENHANCING</p>
    <p class="text-line brand-name">vex lumora</p>
    <p class="text-line product-type">ENERGY DRINK</p>
    <p class="text-line volume">355 ml</p>
  </section>

  <!-- balanced colour version -->
  <section class="front-panel size-small version-balanced can-balanced">
    <svg class="juice-splash" viewBox="0 0 100 100" preserveAspectRatio="none" role="img" aria-label="Flowing pineapple juice splash">
      <path d="M0 8 C20 15 30 30 22 45 C16 58 30 64 45 68 C60 72 78 70 100 78 L100 86 C78 80 58 82 42 78 C24 74 8 64 12 48 C16 34 10 22 0 18 Z" fill="var(--juice)" opacity="0.7"/>
    </svg>
    <div class="lips-art" role="img" aria-label="Illustration of red lips biting a pineapple slice"></div>
    <p class="text-line claim-top">ALL NATURAL</p>
    <p class="text-line claim-main">LIBIDO ENHANCING</p>
    <p class="text-line brand-name">vex lumora</p>
    <p class="text-line product-type">ENERGY DRINK</p>
    <p class="text-line volume">355 ml</p>
  </section>

  <!-- light colour version -->
  <section class="front-panel size-small version-light can-light">
    <svg class="juice-splash" viewBox="0 0 100 100" preserveAspectRatio="none" role="img" aria-label="Flowing pineapple juice splash">
      <path d="M0 8 C20 15 30 30 22 45 C16 58 30 64 45 68 C60 72 78 70 100 78 L100 86 C78 80 58 82 42 78 C24 74 8 64 12 48 C16 34 10 22 0 18 Z" fill="var(--juice)" opacity="0.7"/>
    </svg>
    <div class="lips-art" role="img" aria-label="Illustration of red lips biting a pineapple slice"></div>
    <p class="text-line claim-top">ALL NATURAL</p>
    <p class="text-line claim-main">LIBIDO ENHANCING</p>
    <p class="text-line brand-name">vex lumora</p>
    <p class="text-line product-type">ENERGY DRINK</p>
    <p class="text-line volume">355 ml</p>
  </section>

  <!-- back panel -->
  <section class="can-back">
    <div class="info-block nf-block">
      <div class="nutrition-facts">
        <div class="nf-title">Nutrition Facts</div>
        <div class="nf-row nf-serving"><span>Serving size</span><span>12 fl oz (355 mL)</span></div>
        <div class="nf-calories nf-thick"><div class="label">Amount per serving<span>Calories</span></div><div class="value">90</div></div>
        <div class="nf-dv">% Daily Value*</div>
        <div class="nf-row"><span><b>Total Fat</b> 0g</span><b>0%</b></div>
        <div class="nf-row indent"><span>Saturated Fat 0g</span><b>0%</b></div>
        <div class="nf-row indent"><span>Trans Fat 0g</span><span></span></div>
        <div class="nf-row"><span><b>Cholesterol</b> 0mg</span><b>0%</b></div>
        <div class="nf-row"><span><b>Sodium</b> 5mg</span><b>0%</b></div>
        <div class="nf-row"><span><b>Total Carbohydrate</b> 21g</span><b>8%</b></div>
        <div class="nf-row indent"><span>Dietary Fiber 0g</span><b>0%</b></div>
        <div class="nf-row indent"><span>Total Sugars 18g</span><span></span></div>
        <div class="nf-row indent2"><span>Includes 0g Added Sugars</span><b>0%</b></div>
        <div class="nf-row"><span><b>Protein</b> 0g</span><span></span></div>
        <div class="nf-row nf-thick"><span>Vitamin D 0mcg</span><span>0%</span></div>
        <div class="nf-row"><span>Calcium 18mg</span><span>2%</span></div>
        <div class="nf-row"><span>Iron 0mg</span><span>0%</span></div>
        <div class="nf-row"><span>Potassium 238mg</span><span>6%</span></div>
        <div class="nf-row"><span>Vitamin C 138mg</span><span>150%</span></div>
        <div class="nf-row"><span>Niacin 24mg</span><span>150%</span></div>
        <div class="nf-row"><span>Vitamin B<sub>6</sub> 2.6mg</span><span>150%</span></div>
        <div class="nf-row"><span>Vitamin B<sub>12</sub> 3.6mcg</span><span>150%</span></div>
        <div class="nf-row"><span>Pantothenic Acid 7mg</span><span>140%</span></div>
        <div class="nf-row"><span>Zinc 6mg</span><span>50%</span></div>
        <div class="nf-footnote">*The % Daily Value tells you how much a nutrient in a serving of food contributes to a daily diet. 2,000 calories a day is used for general nutrition advice.</div>
      </div>
    </div>
    <div class="info-block ing-block">
      <p class="ingredients">Allergens: None<br>Ingredients: Filtered Water, Organic Pineapple Juice Concentrate, Organic Natural Flavors, Horny Goat Weed Extract, Citric Acid, L-Arginine, Taurine, Maca Root Extract, Ascorbic Acid, Natural Caffeine from Green Tea, Panax Gingseng, Organic Monk Fruit, Gingko Biloba, Stevia Reb M, Niacinamide, Zinc Citrate, Calcium Pantothenate, Phridoxine Hydrochloride, Cyanocobalamin</p>
    </div>
  </section>

  <!-- flat label -->
  <section class="label-sheet">
    <div class="front-panel size-label">
      <svg class="juice-splash" viewBox="0 0 100 100" preserveAspectRatio="none" role="img" aria-label="Flowing pineapple juice splash">
        <path d="M8 0 C30 6 34 20 30 34 C26 48 40 56 52 62 C64 68 82 70 100 76 L100 84 C82 80 62 80 48 74 C32 66 18 56 22 38 C25 24 18 10 0 4 Z" fill="var(--juice)" opacity="0.7"/>
      </svg>
      <div class="lips-art" role="img" aria-label="Illustration of red lips biting a pineapple slice"></div>
      <p class="text-line claim-top">ALL NATURAL</p>
      <p class="text-line claim-main">LIBIDO ENHANCING</p>
      <p class="text-line brand-name">vex lumora</p>
      <p class="text-line product-type">ENERGY DRINK</p>
      <p class="text-line volume">355 ml</p>
    </div>
    <div class="info-block nf-block">
      <div class="nutrition-facts">
        <div class="nf-title">Nutrition Facts</div>
        <div class="nf-row nf-serving"><span>Serving size</span><span>12 fl oz (355 mL)</span></div>
        <div class="nf-calories nf-thick"><div class="label">Amount per serving<span>Calories</span></div><div class="value">90</div></div>
        <div class="nf-dv">% Daily Value*</div>
        <div class="nf-row"><span><b>Total Fat</b> 0g</span><b>0%</b></div>
        <div class="nf-row indent"><span>Saturated Fat 0g</span><b>0%</b></div>
        <div class="nf-row indent"><span>Trans Fat 0g</span><span></span></div>
        <div class="nf-row"><span><b>Cholesterol</b> 0mg</span><b>0%</b></div>
        <div class="nf-row"><span><b>Sodium</b> 5mg</span><b>0%</b></div>
        <div class="nf-row"><span><b>Total Carbohydrate</b> 21g</span><b>8%</b></div>
        <div class="nf-row indent"><span>Dietary Fiber 0g</span><b>0%</b></div>
        <div class="nf-row indent"><span>Total Sugars 18g</span><span></span></div>
        <div class="nf-row indent2"><span>Includes 0g Added Sugars</span><b>0%</b></div>
        <div class="nf-row"><span><b>Protein</b> 0g</span><span></span></div>
        <div class="nf-row nf-thick"><span>Vitamin D 0mcg</span><span>0%</span></div>
        <div class="nf-row"><span>Calcium 18mg</span><span>2%</span></div>
        <div class="nf-row"><span>Iron 0mg</span><span>0%</span></div>
        <div class="nf-row"><span>Potassium 238mg</span><span>6%</span></div>
        <div class="nf-row"><span>Vitamin C 138mg</span><span>150%</span></div>
        <div class="nf-row"><span>Niacin 24mg</span><span>150%</span></div>
        <div class="nf-row"><span>Vitamin B<sub>6</sub> 2.6mg</span><span>150%</span></div>
        <div class="nf-row"><span>Vitamin B<sub>12</sub> 3.6mcg</span><span>150%</span></div>
        <div class="nf-row"><span>Pantothenic Acid 7mg</span><span>140%</span></div>
        <div class="nf-row"><span>Zinc 6mg</span><span>50%</span></div>
        <div class="nf-footnote">*The % Daily Value tells you how much a nutrient in a serving of food contributes to a daily diet. 2,000 calories a day is used for general nutrition advice.</div>
      </div>
    </div>
    <div class="info-block ing-block">
      <p class="ingredients">Allergens: None<br>Ingredients: Filtered Water, Organic Pineapple Juice Concentrate, Organic Natural Flavors, Horny Goat Weed Extract, Citric Acid, L-Arginine, Taurine, Maca Root Extract, Ascorbic Acid, Natural Caffeine from Green Tea, Panax Gingseng, Organic Monk Fruit, Gingko Biloba, Stevia Reb M, Niacinamide, Zinc Citrate, Calcium Pantothenate, Phridoxine Hydrochloride, Cyanocobalamin</p>
    </div>
  </section>

  <!-- large light front panel -->
  <section class="front-panel size-large version-light can-hero">
    <svg class="juice-splash" viewBox="0 0 100 100" preserveAspectRatio="none" role="img" aria-label="Flowing pineapple juice splash">
      <path d="M0 8 C20 15 30 30 22 45 C16 58 30 64 45 68 C60 72 78 70 100 78 L100 86 C78 80 58 82 42 78 C24 74 8 64 12 48 C16 34 10 22 0 18 Z" fill="var(--juice)" opacity="0.7"/>
    </svg>
    <div class="lips-art" role="img" aria-label="Illustration of red lips biting a pineapple slice"></div>
    <p class="text-line claim-top">ALL NATURAL</p>
    <p class="text-line claim-main">LIBIDO ENHANCING</p>
    <p class="text-line brand-name">vex lumora</p>
    <p class="text-line product-type">ENERGY DRINK</p>
    <p class="text-line volume">355 ml</p>
  </section>

</body>
</html>
```